Corwick Habitat Web

We just need an update/re-design of our existing web site that would include our new company logo and some new photo's. Our current web site can be viewed at www.corwickhabitat.com.au. We would require something very similar to what we have at the moment in terms of content it should all be the same.
The web site would basically act more as a portfolio than one that would generate more business.
We are after a very modern and simple design and maybe something where we can upload our own project photo's and project descriptions as we complete them.

Industry/Entity Type

It Company

```html
<!DOCTYPE html>
<html lang="en">
<head>
<meta charset="utf-8">
<title>Corwick Habitat</title>
<link href="https://fonts.googleapis.com/css2?family=Oswald:wght@400&family=Open+Sans:wght@300;400&family=Lobster+Two:ital@1&display=swap" rel="stylesheet">
<style>
:root{
  --ink:#3a3a3a;
  --muted:#6b6b6b;
  --nav-bg:#2a2828;
  --nav-text:#ffffff;
  --white:#ffffff;
  --band:#7a7a7a;
  --facade-grey:#8d9399;
  --facade-wood:#a0643a;
  --sky:#c9d2da;
  --building:#2e3540;
  --dot:#c8c8c8;
  --dot-active:#333333;
  --social:#a9d8d3;
}
*{margin:0;padding:0;box-sizing:border-box}
html,body{width:760px;height:1200px;overflow:hidden;background:var(--white)}
body{position:relative;font-family:"Open Sans",Arial,sans-serif;color:var(--ink)}
.site-header{position:absolute;top:0;left:0;width:760px;height:108px;display:flex;align-items:center;justify-content:center}
.brand{font-family:"Open Sans",Arial,sans-serif;font-weight:300;font-size:50px;color:#7c7c7c;letter-spacing:-1px}
.main-nav{position:absolute;top:108px;left:0;width:760px;height:35px;background:var(--nav-bg);display:flex;align-items:center}
.main-nav a{font-family:"Oswald",Arial,sans-serif;font-size:14px;color:var(--nav-text);text-decoration:none;text-transform:uppercase;position:absolute;top:8px}
.phone{position:absolute;left:556px;top:3px;display:flex;align-items:center;gap:8px;font-family:"Oswald",Arial,sans-serif;font-size:14px;color:var(--nav-text)}
.hero{position:absolute;top:143px;left:0;width:760px;height:351px;background:linear-gradient(100deg,var(--facade-grey) 0%,var(--facade-wood) 30%,var(--facade-grey) 55%,#4a4f55 75%,var(--sky) 100%)}
.hero-caption{position:absolute;left:123px;top:243px;width:507px;height:86px;background:rgba(255,255,255,.82);text-align:center;padding-top:12px}
.hero-caption p{font-size:12.5px;color:#333;line-height:19px;padding:0 20px}
.hero-caption .tagline{font-family:"Lobster Two",Georgia,cursive;font-style:italic;font-size:15px;margin-top:6px}
.column{position:absolute;top:510px;font-size:8.6px;line-height:12px;color:var(--muted)}
.column h2{font-weight:300;font-size:22px;color:#444;text-align:center;margin-bottom:20px;letter-spacing:.5px}
.why-us{left:87px;width:277px}
.who-we-are{left:408px;width:257px}
.column p{margin-bottom:12px}
.services{list-style:none;margin-left:18px}
.services li{margin-bottom:7px;padding-left:10px;position:relative}
.services li::before{content:"";position:absolute;left:0;top:4px;width:4px;height:4px;background:#999}
.read-more{position:absolute;top:710px;font-size:7.5px;color:#333;text-decoration:underline;text-transform:uppercase}
.latest-projects{position:absolute;top:742px;left:0;width:760px;text-align:center;font-weight:300;font-size:22px;color:#444}
.project-band{position:absolute;top:807px;left:0;width:760px;height:238px;background:var(--band)}
.project-photo{position:absolute;top:787px;left:195px;width:359px;height:277px;background:linear-gradient(160deg,var(--sky) 0%,#e4e8ec 30%,var(--building) 45%,#232830 100%);border:1px solid #ddd}
.arrow{position:absolute;top:900px}
.slider-dots{position:absolute;top:1069px;left:362px;display:flex;gap:3px}
.slider-dots span{width:10px;height:10px;border-radius:50%;background:var(--dot)}
.slider-dots .active{background:var(--dot-active)}
.social{position:absolute;top:1136px;left:89px;display:flex;gap:8px}
.social span{width:30px;height:30px;border-radius:50%;background:var(--social)}
.copyright{position:absolute;top:1161px;left:446px;font-size:7.5px;color:#555}
</style>
</head>
<body>
<header class="site-header"><div class="brand">Corwick Habitat</div></header>
<nav class="main-nav">
  <a href="#" style="left:100px">Home</a>
  <a href="#" style="left:167px">About</a>
  <a href="#" style="left:240px">Recent Projects</a>
  <a href="#" style="left:362px">Our Services</a>
  <a href="#" style="left:470px">Contact</a>
  <div class="phone">
    <svg width="28" height="28" viewBox="0 0 28 28"><circle cx="14" cy="14" r="13" fill="#fff"/><path d="M8 12c0-2 2-3 6-3s6 1 6 3l-2 1-1-2h-6l-1 2zM10 14h8l1 5H9z" fill="#2a2828"/></svg>
    +65 9000 4417
  </div>
</nav>
<section class="hero" role="img" aria-label="Photo of a modern building facade with grey and timber cladding panels">
  <div class="hero-caption">
    <p>The key group of our operating staff have all been involved in the construction industry for well over 20 years.</p>
    <p class="tagline">Lorel ipsum dolors sit amet est di maria</p>
  </div>
</section>
<section class="column why-us">
  <h2>WHY US</h2>
  <p>We specialise in the internal fit outs to</p>
  <ul class="services">
    <li>Industrial Offices</li>
    <li>Multi Storey Offices</li>
    <li>Commercial Projects</li>
    <li>Residential Houses</li>
    <li>External Facades</li>
  </ul>
</section>
<a class="read-more" href="#" style="left:90px">Read more</a>
<section class="column who-we-are">
  <h2>WHO WE ARE</h2>
  <p>Corwick Habitat Pty Ltd was established in 2005 and has been operating in the Sydney area, but has completed numerous projects outside of Sydney.</p>
  <p>The key group of our operating staff have all been involved in the construction industry for well over 20 years.</p>
  <p>Our employees are skilled and trained and have the experience to deliver the best possible product, safely and on time.</p>
  <p>At Corwick Habitat we pride ourselves on working together with our clients in providing the best possible service on schedule and within budget.</p>
</section>
<a class="read-more" href="#" style="left:413px">Read more</a>
<h2 class="latest-projects">LATEST PROJECTS</h2>
<div class="project-band"></div>
<div class="project-photo" role="img" aria-label="Photo of a completed project: dark clad commercial building under a bright sky"></div>
<svg class="arrow" style="left:92px" width="30" height="50" viewBox="0 0 30 50"><path d="M26 3L5 25l21 22" fill="none" stroke="#fff" stroke-width="5"/></svg>
<svg class="arrow" style="left:626px" width="30" height="50" viewBox="0 0 30 50"><path d="M4 3l21 22L4 47" fill="none" stroke="#fff" stroke-width="5"/></svg>
<div class="slider-dots"><span class="active"></span><span></span><span></span><span></span><span></span></div>
<footer>
  <div class="social"><span></span><span></span><span></span></div>
  <p class="copyright">© 2014, All Rights Reserved, Copyright Corwick Habitat Pty Ltd</p>
</footer>
</body>
</html>
```